Industrial & commercial facility maintenance flyer

Design a 2 sided flyer that outlines our core business unit services. One side shall be for our industrial maintenance division while the other will be focused on our commercial maintenance division.

Media from website here: https://files.vornelbox.net/share/7Kq29XzPw4RtLmYc8NdHe5JbVa

Target Market(s)

Industrial and commercial facility maintenance companies and professionals

Industry/Entity Type

Maintenance

Font styles to use
Serif

Colors
ffffff
2f73b4
0455a3
cfdfed

Requirements
Must have
• Several photos of each applicable service. Reference existing website (www.trelcorp.com). Use of the blue and grey scheme of our current logo.
Nice to have
• Our logo design across the top with our contact information on the bottom.

```html
<!DOCTYPE html>
<html lang="en">
<head>
<meta charset="utf-8">
<title>Trelcorp Maintenance Solutions – Two-Sided Flyer</title>
<link rel="stylesheet" href="https://fonts.googleapis.com/css2?family=Montserrat:wght@400;500;600;700&display=swap">
<style>
  :root {
    --white: #ffffff;
    --blue: #2f73b4;
    --blue-deep: #0455a3;
    --blue-pale: #cfdfed;
    --ink: #2b2b2b;
    --grey: #555a60;
    --steel: #6b7075;
  }
  * { box-sizing: border-box; margin: 0; padding: 0; }
  html, body { width: 1200px; height: 1200px; overflow: hidden; background: var(--white); }
  body { position: relative; font-family: "Montserrat", sans-serif; color: var(--ink); }

  .page {
    position: absolute; top: 200px; width: 547px; height: 773px;
    background: var(--white);
    box-shadow: 0 0 6px rgba(0,0,0,0.18);
  }
  .page--industrial { left: 50px; }
  .page--commercial { left: 604px; }
  .page > * { position: absolute; }

  /* brand header */
  .brand-mark {
    left: 161px; top: 25px; width: 42px; height: 42px; border-radius: 50%;
    background: var(--steel);
  }
  .brand-name {
    left: 214px; top: 27px; font-size: 17px; font-weight: 500;
    color: var(--blue-deep); letter-spacing: 0.2px; white-space: nowrap;
  }
  .brand-tagline {
    left: 216px; top: 55px; font-size: 7px; font-weight: 600;
    color: var(--grey); letter-spacing: 2.2px; white-space: nowrap;
  }

  /* photo placeholders */
  .photo { background: linear-gradient(135deg, #8fb0cf, #3a6ea8); }

  /* industrial page hero */
  .hero {
    left: 24px; top: 93px; width: 499px; height: 221px;
    border-radius: 16px 16px 0 0; overflow: hidden;
    background: linear-gradient(180deg, #7fa5c6 0%, #b9c9c8 55%, #3d5d82 100%);
  }
  .hero__band {
    position: absolute; left: 0; bottom: 0; width: 100%; height: 56px;
    background: linear-gradient(90deg, rgba(4,85,163,0.95), rgba(47,115,180,0.85));
    color: var(--white); padding: 9px 16px 0;
  }
  .hero__title { font-size: 17.5px; font-weight: 400; white-space: nowrap; }
  .hero__title strong { font-weight: 700; }
  .hero__sub { font-size: 15px; font-weight: 400; margin-top: 1px; display: flex; align-items: center; gap: 6px; white-space: nowrap; }
  .hero__sub::after { content: ""; width: 216px; height: 1px; background: var(--white); opacity: 0.8; }

  .section-title { font-size: 14px; font-weight: 700; color: var(--blue-deep); }
  .body-copy { font-size: 7.6px; line-height: 10px; text-align: justify; color: var(--ink); }

  .about-title { left: 40px; top: 336px; }
  .about-copy { left: 40px; top: 361px; width: 471px; }
  .services-title { left: 40px; top: 448px; }

  .service-thumb { left: 40px; width: 82px; height: 64px; border-radius: 8px 0 8px 0; }
  .service-label {
    left: 122px; width: 200px; height: 40px; padding: 9px 0 0 20px;
    font-size: 8.6px; line-height: 11px; color: var(--grey); font-weight: 500;
    background: linear-gradient(90deg, #f4f6f8, rgba(255,255,255,0));
  }
  .service--retail { top: 479px; }
  .service--retail.service-label { top: 491px; }
  .service--industrial { top: 558px; }
  .service--industrial.service-label { top: 570px; }
  .service--facility { top: 645px; }
  .service--facility.service-label { top: 657px; }

  .feature {
    left: 300px; top: 478px; width: 210px; height: 119px;
    background: linear-gradient(180deg, #7e8a86 0%, #bfa54a 45%, #56616a 100%);
  }
  .feature__caption {
    position: absolute; left: 0; bottom: 0; width: 100%; height: 22px;
    background: rgba(30,30,30,0.78); color: var(--white);
    font-size: 8.6px; font-weight: 500; text-align: center; line-height: 22px; letter-spacing: 0.2px;
  }
  .feature-copy { left: 310px; top: 608px; width: 190px; }

  /* commercial page */
  .plant {
    left: 24px; top: 93px; width: 498px; height: 221px;
    border-radius: 16px 16px 0 0;
    background: linear-gradient(180deg, #2a5dbf 0%, #8fb3e8 45%, #c9ced3 75%, #8a9097 100%);
  }
  .promo {
    left: 24px; top: 326px; width: 498px; height: 127px; background: var(--blue-deep); overflow: hidden;
  }
  .promo__photo {
    position: absolute; left: 52px; top: 0; width: 196px; height: 100%;
    background: linear-gradient(90deg, rgba(4,85,163,0), rgba(20,50,120,0.75) 50%, rgba(4,85,163,0));
  }
  .promo__title {
    position: absolute; left: 18px; top: 36px; color: var(--white);
    font-size: 18px; font-weight: 700; line-height: 22px;
  }
  .promo__copy {
    position: absolute; left: 264px; top: 24px; width: 209px; color: var(--white);
    font-size: 7.6px; line-height: 10px; text-align: justify;
  }
  .retail-title { left: 42px; top: 470px; font-size: 18px; font-weight: 600; color: var(--ink); white-space: nowrap; }
  .retail-copy { left: 42px; top: 504px; width: 455px; }
  .install-title { left: 44px; top: 566px; font-size: 8.6px; font-weight: 700; color: var(--blue-deep); }
  .install-list { list-style: none; font-size: 8px; line-height: 11px; color: var(--ink); width: 120px; }
  .install-list li { position: relative; padding-left: 12px; }
  .install-list li::before {
    content: ""; position: absolute; left: 1px; top: 3px; width: 5px; height: 5px;
    border: 1px solid var(--steel); border-radius: 50%;
  }
  .install-list li.cont::before { display: none; }
  .install-list--a { left: 44px; top: 592px; }
  .install-list--b { left: 176px; top: 592px; }
  .crew {
    left: 300px; top: 560px; width: 208px; height: 168px; border-radius: 50% 50% 20px 20px;
    background: radial-gradient(ellipse at center, #9aa2a8 0%, #c9cdd0 55%, rgba(255,255,255,0) 75%);
  }

  /* footer */
  .footer { left: 24px; top: 733px; width: 499px; height: 25px; display: flex; }
  .footer__contact {
    width: 252px; height: 100%; background: var(--blue-deep); color: var(--white);
    border-radius: 0 14px 0 0; display: flex; align-items: center; gap: 26px; padding-left: 17px;
    font-size: 7.6px; font-weight: 500;
  }
  .footer__web {
    flex: 1; height: 100%; margin-top: 5px; background: var(--blue-pale); color: var(--ink);
    display: flex; align-items: center; padding-left: 16px; gap: 6px; font-size: 7.6px; letter-spacing: 2.4px;
  }
  .footer__item { display: flex; align-items: center; gap: 6px; white-space: nowrap; }
  .footer__item svg { width: 10px; height: 10px; }
  .social { margin-left: auto; margin-right: 22px; display: flex; gap: 16px; }
  .social span { width: 7px; height: 7px; border-radius: 50%; background: var(--blue-deep); display: block; }
</style>
</head>
<body>

<!-- Industrial side -->
<section class="page page--industrial">
  <div class="brand-mark"></div>
  <div class="brand-name">Trelcorp Maintenance</div>
  <div class="brand-tagline">INDUSTRIAL · COMMERCIAL · RETAIL</div>

  <div class="hero" role="img" aria-label="Photo of a technician holding a wrench in front of a city skyline">
    <div class="hero__band">
      <div class="hero__title"><strong>Facility Maintenance &amp;</strong> Management Solutions</div>
      <div class="hero__sub">Maintaining Your Business</div>
    </div>
  </div>

  <h2 class="section-title about-title">About Trelcorp Maintenance Solutions:</h2>
  <p class="body-copy about-copy">Trelcorp Maintenance Solutions is an integrated, single-source, facility maintenance &amp; management solution for industrial, commercial, and retail clients serving the southeast. TMS leverages our staff of trained maintenance solution experts and network of highly qualified partners to ensure all of our clients maintenance needs are met to their utmost satisfaction. TMS also provides our clients Key Performance Indicators (KPI's) within our powerful Computerized Maintenance Management System (CMMS) to ensure our performance meets their highest expectations.</p>

  <h2 class="section-title services-title">Our Services:</h2>

  <div class="service-thumb photo service--retail" role="img" aria-label="Photo of a maintenance worker carrying a toolbox"></div>
  <div class="service-label service--retail">Retail &amp; Commerical<br>Maintenance Solutions</div>
  <div class="service-thumb photo service--industrial" role="img" aria-label="Photo of a worker in gloves adjusting industrial equipment"></div>
  <div class="service-label service--industrial">Industrial Maintenance<br>Solutions</div>
  <div class="service-thumb photo service--facility" role="img" aria-label="Photo of a handshake over building plans and a hard hat"></div>
  <div class="service-label service--facility">Facility Management<br>Solutions</div>

  <div class="feature" role="img" aria-label="Photo of an industrial plant floor with conveyor machinery">
    <div class="feature__caption">INDUSTRIAL MAINTENANCE SOLUTIONS</div>
  </div>
  <p class="body-copy feature-copy">Our industrial maintenance teams work in the field to handle your needs as quickly as possible, whether to get your critical broken or malfunctioning equipment going again or to support scheduled downtime. We specialize in industrial maintenance, conveyer repair, and overhead door repair, but our industrial services aren't limited to those services. Others include equipment repairs, installation, and adjustment, just to name a few.</p>

  <div class="footer">
    <div class="footer__contact">
      <span class="footer__item"><svg viewBox="0 0 10 10"><path d="M1 3.5 Q5 0.5 9 3.5 L8 5 L6.5 4 L6.5 3 Q5 2.5 3.5 3 L3.5 4 L2 5 Z M2.5 6 h5 v3 h-5 Z" fill="#fff"/></svg>123456789</span>
      <span class="footer__item"><svg viewBox="0 0 10 10"><rect x="0.5" y="2" width="9" height="6" fill="none" stroke="#fff"/><path d="M0.5 2 L5 5.5 L9.5 2" fill="none" stroke="#fff"/></svg>hello@trelcorp.com</span>
    </div>
    <div class="footer__web">
      <svg viewBox="0 0 10 10" width="10" height="10"><circle cx="5" cy="5" r="4.3" fill="none" stroke="#0455a3"/><ellipse cx="5" cy="5" rx="1.8" ry="4.3" fill="none" stroke="#0455a3"/><path d="M0.7 5 h8.6" stroke="#0455a3"/></svg>
      <span>www.trelcorp.com</span>
      <div class="social"><span></span><span></span><span></span></div>
    </div>
  </div>
</section>

<!-- Commercial side -->
<section class="page page--commercial">
  <div class="brand-mark"></div>
  <div class="brand-name">Trelcorp Maintenance</div>
  <div class="brand-tagline">INDUSTRIAL · COMMERCIAL · RETAIL</div>

  <div class="plant" role="img" aria-label="Photo of steel industrial towers and pipework against a blue sky"></div>

  <div class="promo">
    <div class="promo__photo" role="img" aria-label="Photo of a technician in blue overalls carrying a toolbox"></div>
    <h2 class="promo__title">Retail &amp; Commercial<br>Maintenance Solutions</h2>
    <p class="promo__copy">Trelcorp Maintenance Solutions knows how important it is to convert window shoppers to paying customers and to move inventory off your shelves. We ensure that your business is always looking its best with our cost-effective maintenance programs and crews available 24/7 to take care of any equipment or facility malfunction as quickly as possible.</p>
  </div>

  <h2 class="retail-title">Retail Maintenance Services You Can Rely On</h2>
  <p class="body-copy retail-copy">Trelcorp Maintenance Solutions provides services to stand-alone stores and big box stores alike, malls, nightclubs, and more. We work to enhance your image by taking preventative measures, like inspecting equipment for signs of wear or failing components. We service equipment as needed, measuring either by usage or manufacturer recommendations. After maintenance and repairs, our technicians provide an in-depth report on equipment conditions, analyze equipment failure, and discuss future prevention.</p>

  <h3 class="install-title">We install</h3>
  <ul class="install-list install-list--a">
    <li>Doors</li>
    <li>Restroom partitions</li>
    <li class="cont">storefronts</li>
    <li>Flooring, and plumbing</li>
    <li>Repairs include doors</li>
    <li>Storefronts</li>
    <li>Flooring</li>
    <li>Building exteriors</li>
    <li>Plumbing</li>
    <li>Appliances</li>
    <li>Fencing</li>
  </ul>
  <ul class="install-list install-list--b">
    <li>Oading docks</li>
    <li>We take care of</li>
    <li>landscaping, snow</li>
    <li class="cont">removal</li>
    <li>Irrigation systems</li>
    <li>Pest control</li>
    <li class="cont">and other seasonal</li>
    <li class="cont">maintenance as need</li>
    <li class="cont">be when the weather</li>
    <li class="cont">changes.</li>
  </ul>

  <div class="crew" role="img" aria-label="Photo of a team of maintenance workers in hard hats holding toolboxes"></div>

  <div class="footer">
    <div class="footer__contact">
      <span class="footer__item"><svg viewBox="0 0 10 10"><path d="M1 3.5 Q5 0.5 9 3.5 L8 5 L6.5 4 L6.5 3 Q5 2.5 3.5 3 L3.5 4 L2 5 Z M2.5 6 h5 v3 h-5 Z" fill="#fff"/></svg>123456789</span>
      <span class="footer__item"><svg viewBox="0 0 10 10"><rect x="0.5" y="2" width="9" height="6" fill="none" stroke="#fff"/><path d="M0.5 2 L5 5.5 L9.5 2" fill="none" stroke="#fff"/></svg>hello@trelcorp.com</span>
    </div>
    <div class="footer__web">
      <svg viewBox="0 0 10 10" width="10" height="10"><circle cx="5" cy="5" r="4.3" fill="none" stroke="#0455a3"/><ellipse cx="5" cy="5" rx="1.8" ry="4.3" fill="none" stroke="#0455a3"/><path d="M0.7 5 h8.6" stroke="#0455a3"/></svg>
      <span>www.trelcorp.com</span>
      <div class="social"><span></span><span></span><span></span></div>
    </div>
  </div>
</section>

</body>
</html>
```